Business Card for Yachting Management Company

Need a business card design for a new yachting project management company. Attached is the logo for the company.
Our clients are large yacht owners and captains.
Design must be in the style of the logo. Modern, elegant.

Example of data to show:
Peter Hollis
Project Manager
(+34) 612 738 104
peter@quorvane.net
Quorvane Management - Meridel Tower, Office 22 - KRB - Palma de Mallorca

The data above will have to be changed (by me) for the different people in the company over the next years.

Will be printed using PrintNova (Lustre Card Series). They provide these guidelines for the size:
"the actual size of the card is 1050 x 600 pixels. However, the full bleed size is 1083 x 633 pixels, and the safe printing area is 1008 x 558 pixels."

```html
<!DOCTYPE html>
<html lang="en">
<head>
<meta charset="utf-8">
<title>Quorvane Management – Business Card</title>
<link href="https://fonts.googleapis.com/css2?family=Didact+Gothic&family=Mulish:wght@700&display=swap" rel="stylesheet">
<style>
  :root {
    --brand-blue: #0071bc;
    --canvas-grey: #e6e6e6;
    --card-white: #ffffff;
    --ink: #1a1a1a;
  }
  * { margin: 0; padding: 0; box-sizing: border-box; }
  html, body { width: 1022px; height: 1200px; overflow: hidden; }
  body {
    position: relative;
    background: var(--canvas-grey);
    font-family: "Didact Gothic", "Century Gothic", sans-serif;
    color: var(--ink);
  }
  .card {
    position: absolute;
    left: 8px;
    width: 1005px;
    background: var(--card-white);
    overflow: hidden;
  }
  .card--front { top: 8px; height: 574px; }
  .card--back { top: 618px; height: 574px; }

  .band { position: absolute; background: var(--brand-blue); }
  .band--header { left: 56px; top: 0; right: 0; height: 268px; border-bottom-left-radius: 34px; }
  .band--footer { left: 56px; top: 483px; right: 0; height: 91px; border-top-left-radius: 34px; }
  .tab { position: absolute; left: 280px; width: 445px; height: 39px; background: var(--brand-blue); }
  .tab--top { top: 0; border-radius: 0 0 31px 31px; }
  .tab--bottom { bottom: 0; border-radius: 31px 31px 0 0; }

  .identity { position: absolute; left: 96px; top: 62px; color: var(--card-white); }
  .identity__role {
    font-family: "Mulish", "Century Gothic", sans-serif;
    font-weight: 700;
    font-size: 37px;
    line-height: 40px;
    padding-bottom: 1px;
    border-bottom: 2px solid var(--card-white);
    display: inline-block;
    padding-right: 2px;
  }
  .identity__name { font-size: 32px; line-height: 38px; }

  .wordmark {
    position: absolute;
    color: var(--brand-blue);
    text-align: center;
    line-height: 1;
  }
  .wordmark__name { display: block; letter-spacing: 1px; }
  .wordmark__sub { display: block; text-transform: uppercase; }
  .wordmark--small { left: 96px; top: 330px; width: 230px; }
  .wordmark--small .wordmark__name { font-size: 50px; }
  .wordmark--small .wordmark__sub { font-size: 18px; letter-spacing: 6px; margin-top: 10px; }
  .wordmark--large { left: 222px; top: 215px; width: 560px; }
  .wordmark--large .wordmark__name { font-size: 104px; }
  .wordmark--large .wordmark__sub { font-size: 32px; letter-spacing: 11px; margin-top: 20px; }

  .contacts { position: absolute; left: 507px; top: 296px; list-style: none; }
  .contact { position: relative; padding-left: 72px; font-size: 24px; line-height: 27px; }
  .contact__icon { position: absolute; left: 0; fill: var(--brand-blue); }
  .contact--phone { margin-bottom: 25px; }
  .contact--phone .contact__icon { top: -1px; width: 31px; height: 32px; }
  .contact--mail { margin-bottom: 25px; }
  .contact--mail .contact__icon { top: 2px; width: 31px; height: 23px; }
  .contact--address .contact__icon { top: 10px; width: 30px; height: 41px; }
</style>
</head>
<body>
  <section class="card card--front">
    <div class="band band--header"></div>
    <div class="band band--footer"></div>

    <div class="identity">
      <div class="identity__role">Project Manager</div>
      <div class="identity__name">Peter Hollis</div>
    </div>

    <div class="wordmark wordmark--small">
      <span class="wordmark__name">Quorvane</span>
      <span class="wordmark__sub">Management</span>
    </div>

    <ul class="contacts">
      <li class="contact contact--phone">
        <svg class="contact__icon" viewBox="0 0 31 32" aria-hidden="true">
          <path d="M4 1.5c1-1 2.3-1 3.1 0l3.4 4c.7.9.6 2-.2 2.8l-2 1.8c1.8 4 5 7.6 9 9.8l1.8-1.9c.8-.8 2-.9 2.8-.2l4.3 3.3c1 .8 1 2.2.1 3.1l-2.4 2.4c-1 1-2.7 1.3-4 .7C11.5 24.3 6 18.8 2 10.3c-.6-1.3-.3-2.9.7-3.9z"/>
        </svg>
        (+34) 612 738 104
      </li>
      <li class="contact contact--mail">
        <svg class="contact__icon" viewBox="0 0 31 23" aria-hidden="true">
          <path d="M0 0h31v2L15.5 14 0 2z"/>
          <path d="M0 6l15.5 12L31 6v17H0z"/>
        </svg>
        peter@quorvane.net
      </li>
      <li class="contact contact--address">
        <svg class="contact__icon" viewBox="0 0 30 41" aria-hidden="true">
          <path fill-rule="evenodd" d="M15 0a15 15 0 0 1 12.5 23.3L15 41 2.5 23.3A15 15 0 0 1 15 0zm0 8a7 7 0 1 0 0 14 7 7 0 0 0 0-14z"/>
        </svg>
        Quorvane Management - Meridel Tower,<br>Office 22 - KRB - Palma de Mallorca
      </li>
    </ul>
  </section>

  <section class="card card--back">
    <div class="tab tab--top"></div>
    <div class="wordmark wordmark--large">
      <span class="wordmark__name">Quorvane</span>
      <span class="wordmark__sub">Management</span>
    </div>
    <div class="tab tab--bottom"></div>
  </section>
</body>
</html>
```